Menu Design for coffee shop/cafe

We need a menu designed for our cafe/coffee shop. We want to go for a pretty floral/rustic look, white washed, dusty pinks and beige. Our logo has a birdcage, and the cafe decor will have birdcages, flowers to match this. We would like for everything to fit onto an A3 or A2 double sided. including drinks, and we are looking at a separate smaller option for kids menu, which can include a colouring in section on the one side.

```html
<!DOCTYPE html>
<html lang="en">
<head>
<meta charset="utf-8">
<title>The Linden Room — Menu</title>
<link href="https://fonts.googleapis.com/css2?family=Anton&family=Josefin+Sans:wght@700&family=Montserrat:wght@700&display=swap" rel="stylesheet">
<style>
  :root {
    --paper: #f8f3ef;
    --ink: #151515;
    --muted: #5a5654;
    --rose: #d9a08a;
    --accent: #9a3a1c;
    --card: #efe9e6;
    --navy: #1f2438;
    --teal: #5fc3b8;
    --cream: #efdcb8;
    --wine: #7d1a2c;
  }
  * { margin: 0; padding: 0; box-sizing: border-box; }
  html, body { width: 849px; height: 1200px; overflow: hidden; background: var(--paper); }
  .menu {
    position: relative; width: 849px; height: 1200px; overflow: hidden;
    background:
      radial-gradient(circle at 22% 14%, rgba(240,200,205,.35), transparent 28%),
      radial-gradient(circle at 88% 18%, rgba(210,210,215,.25), transparent 22%),
      var(--paper);
    color: var(--ink);
  }
  .frame { position: absolute; inset: 0; }
  .floral { position: absolute; }
  .floral--top-left {
    left: 0; top: 0; width: 180px; height: 220px;
    background:
      radial-gradient(circle at 80px 70px, var(--navy) 0 48px, transparent 50px),
      radial-gradient(circle at 150px 40px, var(--teal) 0 18px, transparent 20px),
      radial-gradient(circle at 60px 125px, var(--teal) 0 24px, transparent 26px),
      radial-gradient(circle at 20px 190px, var(--navy) 0 8px, transparent 9px);
  }
  .floral--bottom-right {
    right: 0; bottom: 0; width: 260px; height: 200px;
    background:
      radial-gradient(circle at 190px 90px, var(--cream) 0 50px, transparent 52px),
      radial-gradient(circle at 110px 150px, var(--cream) 0 42px, transparent 44px),
      radial-gradient(circle at 150px 110px, var(--wine) 0 18px, transparent 20px),
      radial-gradient(circle at 40px 150px, #7a4c8c 0 8px, transparent 9px);
  }
  .brand {
    position: absolute; left: 0; width: 849px; top: 150px; text-align: center;
    font-family: "Josefin Sans", sans-serif; font-weight: 700; font-size: 26px;
    color: var(--rose); letter-spacing: 1px;
  }
  .section { position: absolute; }
  .section__title {
    font-family: "Anton", sans-serif; font-size: 32px; line-height: 1; letter-spacing: 1.5px;
    padding-bottom: 8px; border-bottom: 2px solid var(--ink); margin-bottom: 18px;
  }
  .item { position: relative; height: 55px; }
  .item__name {
    font-family: "Josefin Sans", sans-serif; font-weight: 700; font-size: 13.5px;
    letter-spacing: .6px; line-height: 14px; text-transform: uppercase;
  }
  .item__price {
    position: absolute; right: 0; top: 0; font-family: "Anton", sans-serif;
    font-size: 14px; line-height: 14px; letter-spacing: .5px;
  }
  .item__price--accent { color: var(--accent); }
  .item__desc {
    margin-top: 5px; width: 240px; font-family: "Montserrat", sans-serif; font-weight: 700;
    font-size: 7px; line-height: 10.5px; color: var(--muted); text-transform: uppercase;
  }
  .coffee { left: 108px; top: 236px; width: 276px; }
  .drinks { left: 466px; top: 236px; width: 275px; }
  .special { left: 108px; top: 755px; width: 276px; }
  .kids-card {
    position: absolute; left: 468px; top: 654px; width: 270px; height: 352px;
    background: var(--card); box-shadow: 0 0 6px rgba(0,0,0,.12);
  }
  .kids { left: 12px; top: 20px; width: 250px; }
  .kids .section__title { margin-bottom: 14px; }
  .kids .item { padding-left: 5px; padding-right: 10px; }
  .kids .item__price { right: 10px; }
  .kids .item__desc { width: 190px; }
  .contact {
    position: absolute; left: 0; width: 849px; top: 1063px; text-align: center;
    font-family: "Anton", sans-serif; font-size: 27px; letter-spacing: 1px;
  }
</style>
</head>
<body>
<main class="menu">
  <svg class="frame" width="849" height="1200" aria-hidden="true">
    <g stroke="#1a1a1a" stroke-linecap="round" fill="none">
      <path d="M172 37 L810 38" stroke-width="4"/>
      <path d="M176 41 L806 40" stroke-width="1.5"/>
      <path d="M810 36 L811 330" stroke-width="4"/>
      <path d="M806 650 L808 1030" stroke-width="4"/>
      <path d="M42 208 L43 482" stroke-width="4"/>
      <path d="M41 624 L42 1104" stroke-width="4"/>
      <path d="M124 1144 L688 1142" stroke-width="4"/>
      <path d="M130 1140 L680 1139" stroke-width="1.5"/>
      <path d="M102 213 L744 212" stroke-width="2.5"/>
    </g>
  </svg>

  <div class="floral floral--top-left" role="img" aria-label="Dark navy roses with teal blooms and berry sprigs"></div>
  <div class="floral floral--bottom-right" role="img" aria-label="Cream roses with burgundy blooms and purple berries"></div>

  <div class="brand">The Linden Room</div>

  <section class="section coffee">
    <h2 class="section__title">COFFEE</h2>
    <div class="item"><div class="item__name">Cafe Latte</div><div class="item__price">$ 08</div><p class="item__desc">Lorem ipsum is simply dummy text of the printing and typesetting industry.</p></div>
    <div class="item"><div class="item__name">Cappuccino</div><div class="item__price">$ 08</div><p class="item__desc">Lorem ipsum is simply dummy text of the printing and typesetting industry.</p></div>
    <div class="item"><div class="item__name">Americano</div><div class="item__price">$ 15</div><p class="item__desc">Lorem ipsum is simply dummy text of the printing and typesetting industry.</p></div>
    <div class="item"><div class="item__name">Killer Bee</div><div class="item__price">$ 08</div><p class="item__desc">Lorem ipsum is simply dummy text of the printing and typesetting industry.</p></div>
    <div class="item"><div class="item__name">Vanilla Latte</div><div class="item__price">$ 14</div><p class="item__desc">Lorem ipsum is simply dummy text of the printing and typesetting industry.</p></div>
    <div class="item"><div class="item__name">Caramel Latte</div><div class="item__price">$ 08</div><p class="item__desc">Lorem ipsum is simply dummy text of the printing and typesetting industry.</p></div>
    <div class="item"><div class="item__name">Espresso</div><div class="item__price">$ 12</div><p class="item__desc">Lorem ipsum is simply dummy text of the printing and typesetting industry.</p></div>
    <div class="item"><div class="item__name">Macchiato</div><div class="item__price">$ 10</div><p class="item__desc">Lorem ipsum is simply dummy text of the printing and typesetting industry.</p></div>
  </section>

  <section class="section drinks">
    <h2 class="section__title">DRINKS</h2>
    <div class="item"><div class="item__name">Cucumber</div><div class="item__price item__price--accent">$ 10</div><p class="item__desc">Lorem ipsum is simply dummy text of the printing and typesetting industry.</p></div>
    <div class="item"><div class="item__name">Lemon Lime</div><div class="item__price">$ 05</div><p class="item__desc">Lorem ipsum is simply dummy text of the printing and typesetting industry.</p></div>
    <div class="item"><div class="item__name">Cream Soda</div><div class="item__price">$ 08</div><p class="item__desc">Lorem ipsum is simply dummy text of the printing and typesetting industry.</p></div>
    <div class="item"><div class="item__name">Coffee Soda</div><div class="item__price">$ 04</div><p class="item__desc">Lorem ipsum is simply dummy text of the printing and typesetting industry.</p></div>
    <div class="item"><div class="item__name">Blueberry</div><div class="item__price">$ 06</div><p class="item__desc">Lorem ipsum is simply dummy text of the printing and typesetting industry.</p></div>
    <div class="item"><div class="item__name">Concord Grape</div><div class="item__price">$ 03</div><p class="item__desc">Lorem ipsum is simply dummy text of the printing and typesetting industry.</p></div>
  </section>

  <section class="section special">
    <h2 class="section__title">SPECIAL COFFEE DAY</h2>
    <div class="item"><div class="item__name">Best Drink Ever</div><div class="item__price">$ 10</div><p class="item__desc">Lorem ipsum is simply dummy text of the printing and typesetting industry.</p></div>
    <div class="item"><div class="item__name">Honey Latte</div><div class="item__price">$ 05</div><p class="item__desc">Lorem ipsum is simply dummy text of the printing and typesetting industry.</p></div>
    <div class="item"><div class="item__name">Mint Mocha Latte</div><div class="item__price">$ 08</div><p class="item__desc">Lorem ipsum is simply dummy text of the printing and typesetting industry.</p></div>
    <div class="item"><div class="item__name">Caramel Mocha</div><div class="item__price">$ 04</div><p class="item__desc">Lorem ipsum is simply dummy text of the printing and typesetting industry.</p></div>
  </section>

  <aside class="kids-card">
    <section class="section kids">
      <h2 class="section__title">KIDS MENU</h2>
      <div class="item"><div class="item__name">Best Drink Ever</div><div class="item__price">$ 10</div><p class="item__desc">Lorem ipsum is simply dummy text of the and typesetting industry.</p></div>
      <div class="item"><div class="item__name">Honey Latte</div><div class="item__price">$ 05</div><p class="item__desc">Lorem ipsum is simply dummy text of the and typesetting industry.</p></div>
      <div class="item"><div class="item__name">Mint Mocha Latte</div><div class="item__price">$ 08</div><p class="item__desc">Lorem ipsum is simply dummy text of the and typesetting industry.</p></div>
      <div class="item"><div class="item__name">Honey Latte</div><div class="item__price">$ 05</div><p class="item__desc">Lorem ipsum is simply dummy text of the and typesetting industry.</p></div>
      <div class="item"><div class="item__name">Mint Mocha Latte</div><div class="item__price">$ 08</div><p class="item__desc">Lorem ipsum is simply dummy text of the and typesetting industry.</p></div>
    </section>
  </aside>

  <p class="contact">CONTACT US: 000 000 0000</p>
</main>
</body>
</html>
```